New boutique IT consultancy needs business card

I need a business card and logo for my IT consultancy business, called 'Quenbrylle' . I want it to make me look bigger than I am. I want it to look classy, and modern. Simple design, that will be easy for me to translate into my webpage etc. The business card should be bold, and different.

The logo should emphasise the 'y' as used in quenbrylle

Target Market(s)

IT divisions in other companies

Industry/Entity Type

Business

Contact Information for Business Card

Marcel Thornby
Director
+61 437 819 063
mthornby@quenbrylle-mail.com

```html
<!DOCTYPE html>
<html lang="en">
<head>
<meta charset="utf-8">
<title>Quenbrylle — Business Card</title>
<link href="https://fonts.googleapis.com/css2?family=Comfortaa:wght@300;400;700&display=swap" rel="stylesheet">
<style>
  :root {
    --backdrop: #e6e7e9;
    --card-white: #ffffff;
    --card-blue: #0c4a9c;
    --ink-dark: #1d2530;
    --ink-blue: #1a57b0;
    --ink-grey: #4a4f57;
    --ink-silver: #c7ccd4;
  }
  * { margin: 0; padding: 0; box-sizing: border-box; }
  html, body {
    width: 1200px; height: 1021px; overflow: hidden;
    background: var(--backdrop);
    font-family: "Comfortaa", sans-serif;
  }
  .canvas { position: relative; width: 1200px; height: 1021px; }

  .card {
    position: absolute;
    width: 560px; height: 320px;
    box-shadow: 0 6px 18px rgba(0,0,0,0.12);
  }
  .card-front { left: 90px; top: 90px; background: var(--card-white); }
  .card-back  { left: 550px; top: 460px; background: var(--card-blue); }

  .wordmark {
    font-family: "Comfortaa", sans-serif;
    font-weight: 700;
    letter-spacing: 0.06em;
    text-transform: uppercase;
    white-space: nowrap;
  }
  .card-front .wordmark {
    position: absolute; left: 40px; top: 170px;
    font-size: 26px; color: var(--ink-dark);
  }
  .card-back .wordmark {
    position: absolute; left: 0; right: 0; top: 138px; text-align: center;
    font-size: 40px; color: var(--ink-silver);
  }

  .contact { position: absolute; left: 300px; top: 90px; color: var(--ink-grey); }
  .contact-name { font-size: 22px; font-weight: 300; color: var(--ink-grey); }
  .contact-role { font-size: 14px; color: var(--ink-blue); margin-top: 4px; }
  .contact-list { list-style: none; margin-top: 22px; font-size: 12.5px; }
  .contact-list li { display: flex; align-items: center; gap: 12px; margin-bottom: 14px; }
  .contact-list svg { width: 14px; height: 14px; fill: var(--ink-blue); flex: none; }

  .brand-lockup {
    position: absolute; left: 70px; top: 880px;
  }
  .brand-lockup .wordmark { font-size: 58px; color: var(--ink-dark); }
</style>
</head>
<body>
<main class="canvas">
  <section class="card card-front">
    <div class="wordmark">Quenbrylle</div>
    <div class="contact">
      <div class="contact-name">Marcel Thornby</div>
      <div class="contact-role">Director</div>
      <ul class="contact-list">
        <li>
          <svg viewBox="0 0 16 16" aria-hidden="true"><path d="M3 2h3l1 4-2 1c1 2 2 3 4 4l1-2 4 1v3c0 1-1 1-2 1C6 14 2 10 2 4c0-1 0-2 1-2z"/></svg>
          <span>+61 437 819 063</span>
        </li>
        <li>
          <svg viewBox="0 0 16 16" aria-hidden="true"><path d="M1 3h14v10H1z M2 4l6 5 6-5" fill="none" stroke="#1a57b0" stroke-width="1.4"/></svg>
          <span>mthornby@quenbrylle-mail.com</span>
        </li>
      </ul>
    </div>
  </section>

  <section class="card card-back">
    <div class="wordmark">Quenbrylle</div>
  </section>

  <div class="brand-lockup">
    <div class="wordmark">Quenbrylle</div>
  </div>
</main>
</body>
</html>
```